Fishing Tackle Store needs a gift box design

I need a contemporary design for the interior of a 'mystery' tackle gift box. We are a high end tackle store in Far North QLD, Australia called "Driftwood Reel Outfitters'. I have attached our logo for reference. Ideally I would like to include 3-5 fish facts (relative to our location and I can supply these) to give the gift boxes a point of difference, however I am really open to any creative design. Our main fish species are Barramundi, Tuna, Black Marlin, Giant Trevally, Sailfish, Wahoo, Spanish Mackerel. Colour - black / white. We are wanting these boxes to gain traction on social media so looking for an epic design! Thank you!

```html
<!DOCTYPE html>
<html lang="en">
<head>
<meta charset="utf-8">
<title>Spanish Mackerel – Fish Facts Box Insert</title>
<link rel="stylesheet" href="https://fonts.googleapis.com/css2?family=Anton&family=Source+Sans+3:wght@400&display=swap">
<style>
  :root {
    --ink: #000000;
    --paper: #ffffff;
    --rule: #d9d9d9;
    --fish-light: #d8d8d8;
    --fish-mid: #8a8a8a;
    --fish-dark: #2a2a2a;
  }
  * { box-sizing: border-box; margin: 0; padding: 0; }
  html, body { width: 1200px; height: 943px; overflow: hidden; background: var(--ink); }
  .insert {
    position: relative;
    width: 1200px;
    height: 943px;
    background: var(--ink);
    color: var(--paper);
    font-family: "Source Sans 3", "Helvetica Neue", Arial, sans-serif;
  }
  .frame {
    position: absolute;
    border: 1px solid var(--rule);
  }
  .frame--outer { left: 45px; top: 52px; width: 1109px; height: 843px; }
  .frame--inner { left: 62px; top: 65px; width: 1076px; height: 813px; opacity: .7; }

  .size-badge {
    position: absolute;
    width: 310px;
    height: 310px;
    border: 2px solid var(--paper);
    border-radius: 50%;
    background: var(--ink);
    text-align: center;
  }
  .size-badge--average { left: 23px; top: 103px; }
  .size-badge--trophy { left: 866px; top: 103px; }
  .size-badge__label {
    position: absolute;
    left: 0; right: 0;
    top: 62px;
    font-size: 15px;
    letter-spacing: 4px;
  }
  .size-badge__value {
    position: absolute;
    left: 0; right: 0;
    top: 100px;
    font-family: "Anton", Impact, sans-serif;
    font-size: 132px;
    line-height: 1;
  }
  .size-badge__unit { font-size: 48px; margin-left: 4px; }

  .species-title {
    position: absolute;
    left: 380px;
    top: 100px;
    width: 440px;
    text-align: center;
    font-family: "Anton", Impact, sans-serif;
    font-weight: 400;
    font-size: 124px;
    line-height: 96px;
    letter-spacing: 1px;
  }

  .species-art {
    position: absolute;
    left: 83px;
    top: 337px;
    width: 1030px;
    height: 292px;
  }

  .fact {
    position: absolute;
    top: 690px;
    text-align: center;
  }
  .fact--marlin { left: 70px; width: 350px; }
  .fact--sailfish { left: 465px; width: 290px; }
  .fact--barra { left: 790px; width: 350px; }
  .fact__name {
    font-family: "Anton", Impact, sans-serif;
    font-weight: 400;
    font-size: 56px;
    line-height: 64px;
  }
  .fact__text {
    margin-top: 6px;
    font-size: 16.5px;
    line-height: 29px;
  }
  .divider {
    position: absolute;
    top: 684px;
    width: 1px;
    height: 162px;
    background: var(--rule);
  }
</style>
</head>
<body>
<main class="insert">
  <div class="frame frame--outer"></div>
  <div class="frame frame--inner"></div>

  <div class="size-badge size-badge--average">
    <p class="size-badge__label">AVERAGE SIZE</p>
    <p class="size-badge__value">8<span class="size-badge__unit">KG</span></p>
  </div>

  <h1 class="species-title">SPANISH<br>MACKEREL</h1>

  <div class="size-badge size-badge--trophy">
    <p class="size-badge__label">TROPHY SIZE</p>
    <p class="size-badge__value">30<span class="size-badge__unit">KG</span></p>
  </div>

  <svg class="species-art" viewBox="0 0 1030 292" role="img" aria-label="Black and white illustration of a Spanish mackerel swimming left">
    <defs>
      <linearGradient id="fishTone" x1="0" y1="0" x2="0" y2="1">
        <stop offset="0" stop-color="var(--fish-dark)"/>
        <stop offset=".45" stop-color="var(--fish-mid)"/>
        <stop offset=".75" stop-color="var(--fish-light)"/>
        <stop offset="1" stop-color="var(--fish-mid)"/>
      </linearGradient>
    </defs>
    <ellipse cx="500" cy="150" rx="500" ry="95" fill="url(#fishTone)"/>
  </svg>

  <section class="fact fact--marlin">
    <h2 class="fact__name">BLACK MARLIN</h2>
    <p class="fact__text">The black marlin is the only marlin<br>with non-retractable fins.</p>
  </section>

  <div class="divider" style="left:440px"></div>
  <div class="divider" style="left:456px"></div>

  <section class="fact fact--sailfish">
    <h2 class="fact__name">SAILFISH</h2>
    <p class="fact__text">Sailfish are considered the fastest<br>fish in the sea, reaching top speeds<br>of 70 miles per hour.</p>
  </section>

  <div class="divider" style="left:762px"></div>
  <div class="divider" style="left:778px"></div>

  <section class="fact fact--barra">
    <h2 class="fact__name">BARRAMUNDI</h2>
    <p class="fact__text">Most barra start their lives as males,<br>then switch to female, that’s why<br>most of the big ‘meterys’ are female.</p>
  </section>
</main>
</body>
</html>
```